UI Graphics Design For Web Based Home Control

Hi,
Our company Brell Systems is looking for user interface graphics in form of *.psd for home control user interface for a real system which can be used on mobile and PC/MAC.
In Ideal solution, the same interface should be used on mobile, tablets, computers. It changes only to fit the size of the screen. The bigger the screen, the more options you have visible on same view. The user should get familiar interface logic with every device.
The design should have at least the following views covered:
1. Lights view
- List of rooms and lamps
- You can see the status and you can switch it on/off
2. Login view
- Logo (company logo attached)
- Username field
- Password field
3. Dashboard view
- Indicating and choosing home/not home
- Can go to lights view
- Can go to settings view
- Notification list
4. Settings view
- View and edit users
- View and edit lights
Show us your view of ideal home control UI :)
Updates
Time of the project extended by 10 days to receive more designs. If someone sees that the reward should be increased, please also provide the amount expected with the first design. We are willing to increase the amount paid if we see a good design.
Reason: We expect to receive more designs. We are willing to increase the reward if we see good and acceptable designs. Please provide the amount expected with the first design. Project will end with full designs available.
We added our input as an attachment how we see the UI logic. Please have a look into the file.
Reason: We are seeing some good designs. We increased the budget. We are still not where we expect.

```html
<!DOCTYPE html>
<html lang="en">
<head>
<meta charset="utf-8">
<title>Brell Systems – Home Control Dashboard</title>
<link rel="stylesheet" href="https://fonts.googleapis.com/css2?family=Nunito+Sans:wght@300;400;600&display=swap">
<style>
  :root {
    --bg: #cfcfcf;
    --shell: #e4e4e4;
    --panel: #ececec;
    --card: #fbfbfb;
    --navy: #1d3f7a;
    --text: #3c3c3c;
    --muted: #8c8c8c;
    --icon: #a9a9a9;
    --blue-top: #5cc4f2;
    --blue-bottom: #2d7fd0;
    --dark-top: #3a3a3a;
    --dark-bottom: #0c0c0c;
    --warn: #e2d33a;
    --line: #d4d4d4;
  }
  * { box-sizing: border-box; margin: 0; padding: 0; }
  html, body { width: 1200px; height: 990px; overflow: hidden; }
  body {
    background: var(--bg);
    font-family: "Nunito Sans", sans-serif;
    color: var(--text);
    position: relative;
  }
  .shell {
    position: absolute; left: 17px; top: 22px; width: 1166px; height: 948px;
    background: linear-gradient(135deg, #efefef 0%, var(--shell) 60%, #dedede 100%);
    border-radius: 14px;
  }
  .content {
    position: absolute; left: 430px; top: 48px; width: 731px; height: 896px;
    background: linear-gradient(180deg, #f0f0f0, var(--panel));
    border-radius: 10px; overflow: hidden;
  }
  .content .disc {
    position: absolute; left: 252px; top: 664px; width: 210px; height: 210px;
    border-radius: 50%; background: #e0e0e0;
  }
  .brand {
    position: absolute; left: 86px; top: 92px;
    display: flex; align-items: center; gap: 14px;
    font-size: 44px; font-weight: 600; color: var(--navy); letter-spacing: 0.5px;
  }
  .brand .mark { width: 22px; height: 22px; border-radius: 50%; background: var(--navy); }
  .presence {
    position: absolute; left: 56px; top: 227px; width: 324px; height: 55px;
    display: flex; border-radius: 8px; overflow: hidden;
    box-shadow: 0 1px 2px rgba(0,0,0,.35);
    font-size: 20px; color: #fff; font-weight: 400;
  }
  .presence span { display: flex; align-items: center; gap: 12px; padding-left: 26px; }
  .presence .home { width: 162px; background: linear-gradient(var(--blue-top), var(--blue-bottom)); }
  .presence .away { flex: 1; background: linear-gradient(var(--dark-top), var(--dark-bottom)); padding-left: 12px; }
  .nav-item {
    position: absolute; left: 58px; height: 74px; width: 330px;
    display: flex; align-items: center;
  }
  .nav-item::before {
    content: ""; position: absolute; left: 36px; top: 8px; right: 0; bottom: 8px;
    background: linear-gradient(90deg, #d9d9d9, rgba(230,230,230,0)); border-radius: 0 6px 6px 0;
  }
  .nav-item .knob {
    position: relative; width: 74px; height: 74px; border-radius: 50%;
    background: linear-gradient(#55b6e6, #1f4f9a);
    display: flex; align-items: center; justify-content: center;
  }
  .nav-item .knob i {
    width: 52px; height: 52px; border-radius: 50%; background: linear-gradient(#fafafa, #dcdcdc);
    display: flex; align-items: center; justify-content: center;
  }
  .nav-item .label { position: relative; margin-left: 38px; font-size: 27px; color: var(--navy); }
  .nav-lights { top: 325px; }
  .nav-settings { top: 414px; }
  .notice {
    position: absolute; left: 41px; top: 829px; width: 369px; height: 114px;
    background: #f6f6f6; border-radius: 6px; padding: 6px;
  }
  .notice-inner {
    height: 100%; background: var(--card); border-radius: 4px;
    box-shadow: 0 2px 3px rgba(0,0,0,.18);
    display: flex; align-items: flex-start; gap: 26px; padding: 24px 0 0 24px;
  }
  .notice p { font-size: 17px; line-height: 22px; color: #444; }
  .section-title {
    position: absolute; left: 500px; display: flex; align-items: center; gap: 16px;
    font-size: 30px; color: var(--navy);
  }
  .title-lights { top: 80px; }
  .title-sensors { top: 438px; }
  .card {
    position: absolute; left: 470px; width: 662px;
    background: linear-gradient(#ffffff, #f3f3f3);
    border-radius: 8px; box-shadow: 0 3px 3px rgba(0,0,0,.15);
  }
  .card-lights { top: 158px; height: 234px; }
  .card-sensors { top: 509px; height: 228px; }
  .row { position: absolute; left: 36px; right: 40px; display: flex; align-items: center; height: 40px; }
  .row svg { width: 26px; flex: none; }
  .row .name { margin-left: 16px; font-size: 25px; font-weight: 300; flex: 1; color: #333; }
  .row .value { width: 130px; font-size: 26px; font-weight: 300; color: var(--muted); }
  .switch {
    width: 108px; height: 40px; border-radius: 20px; border: 2px solid #bdbdbd;
    background: linear-gradient(#f4f4f4, #e6e6e6); position: relative;
    font-size: 22px; font-weight: 600; color: #777; padding-left: 46px; line-height: 36px;
  }
  .switch::before {
    content: ""; position: absolute; left: 1px; top: 1px; width: 34px; height: 34px;
    border-radius: 50%; background: linear-gradient(#ffffff, #e2e2e2); box-shadow: 0 1px 2px rgba(0,0,0,.4);
  }
</style>
</head>
<body>
  <div class="shell"></div>
  <div class="content"><div class="disc"></div></div>

  <div class="brand"><span class="mark"></span>Brell Systems</div>

  <div class="presence">
    <span class="home">
      <svg width="22" height="22" viewBox="0 0 22 22"><path d="M11 2 1 11h3v9h5v-6h4v6h5v-9h3z" fill="#fff"/></svg>Home
    </span>
    <span class="away">
      <svg width="22" height="22" viewBox="0 0 22 22"><rect x="2" y="2" width="18" height="18" fill="none" stroke="#fff" stroke-width="2"/><path d="M6 16 16 6M10 6h6v6" stroke="#fff" stroke-width="2" fill="none"/></svg>Not Home
    </span>
  </div>

  <div class="nav-item nav-lights">
    <span class="knob"><i><svg width="22" height="26" viewBox="0 0 22 26"><circle cx="11" cy="9" r="8" fill="none" stroke="#aaa" stroke-width="2"/><rect x="7" y="18" width="8" height="6" fill="#aaa"/></svg></i></span>
    <span class="label">Lights View</span>
  </div>
  <div class="nav-item nav-settings">
    <span class="knob"><i><svg width="26" height="26" viewBox="0 0 26 26"><circle cx="13" cy="13" r="9" fill="none" stroke="#aaa" stroke-width="4" stroke-dasharray="4 3"/><circle cx="13" cy="13" r="4" fill="#aaa"/></svg></i></span>
    <span class="label">Settings View</span>
  </div>

  <div class="notice">
    <div class="notice-inner">
      <svg width="56" height="48" viewBox="0 0 56 48"><path d="M28 2 54 46H2z" fill="var(--warn)"/><rect x="25.5" y="16" width="5" height="18" fill="#fff"/><rect x="25.5" y="37" width="5" height="5" fill="#fff"/></svg>
      <p>Turn off the lights sharp<br>at 6: AM</p>
    </div>
  </div>

  <div class="section-title title-lights">
    <svg width="26" height="38" viewBox="0 0 26 38"><circle cx="13" cy="12" r="10" fill="none" stroke="var(--icon)" stroke-width="2"/><rect x="8" y="24" width="10" height="10" rx="2" fill="var(--icon)"/></svg>
    Lights
  </div>
  <div class="card card-lights">
    <div class="row" style="top:30px">
      <svg height="32" viewBox="0 0 26 32"><rect x="10" y="2" width="6" height="22" rx="3" fill="var(--icon)"/><circle cx="13" cy="26" r="5" fill="var(--icon)"/></svg>
      <span class="name">Home Temp</span><span class="value">19.9 °C</span>
    </div>
    <div class="row" style="top:96px">
      <svg height="26" viewBox="0 0 26 26"><circle cx="13" cy="13" r="5" fill="none" stroke="var(--icon)" stroke-width="2"/><path d="M13 1v6M13 19v6M1 13h6M19 13h6M4 4l4 4M18 18l4 4M22 4l-4 4M8 18l-4 4" stroke="var(--icon)" stroke-width="2"/></svg>
      <span class="name">Home Humidity</span><span class="value">58%</span>
    </div>
    <div class="row" style="top:162px">
      <svg height="32" viewBox="0 0 26 32"><circle cx="13" cy="11" r="9" fill="none" stroke="var(--icon)" stroke-width="2"/><rect x="9" y="22" width="8" height="8" rx="2" fill="var(--icon)"/></svg>
      <span class="name">Light 14&nbsp; Home</span><span class="switch">OFF</span>
    </div>
  </div>

  <div class="section-title title-sensors">
    <svg width="32" height="32" viewBox="0 0 32 32"><circle cx="16" cy="16" r="14" fill="none" stroke="var(--icon)" stroke-width="2"/><circle cx="16" cy="16" r="8" fill="none" stroke="var(--icon)" stroke-width="2"/><path d="M16 16 28 8" stroke="var(--icon)" stroke-width="2"/></svg>
    Sensors
  </div>
  <div class="card card-sensors">
    <div class="row" style="top:41px">
      <svg height="32" viewBox="0 0 26 32"><rect x="10" y="2" width="6" height="22" rx="3" fill="var(--icon)"/><circle cx="13" cy="26" r="5" fill="var(--icon)"/></svg>
      <span class="name">Bathroom Temp</span><span class="value">20.3 °C</span>
    </div>
    <div class="row" style="top:107px">
      <svg height="32" viewBox="0 0 26 32"><rect x="10" y="2" width="6" height="22" rx="3" fill="var(--icon)"/><circle cx="13" cy="26" r="5" fill="var(--icon)"/></svg>
      <span class="name">Bathroom Humidity</span><span class="value">61%</span>
    </div>
  </div>
</body>
</html>
```